依頼詳細
名刺裏面リニューアルのため、裏面のデザインをお願いいたします。
基本的にテキストのみの情報を掲載したいと思っています。
記載項目
①キャッチ
日本で唯一、新規営業に特化した営業支援会社です。

②弊社サービス紹介
・クヌーデル帳:
日本で唯一、新規営業に特化した営業ツール。
営業会社自ら、現場の声と使いやすさをもとにシステムを開発いたしました。

・企業リスト作成:
どんな営業活動も、まずはベストの営業先の見極めから。
社内、そしてWEBのデータを収集・分析を行ない、結果につながる、確度の高い企業リストを作成いたします。

・FAX集客支援:
中小企業、BtoBには非常に有効なFAXの原稿作成、またFAX配信を代行いたします。

③グループ会社一覧(社名の記載のみでかまいません)
・株式会社クレモアリス
・株式会社ミルベーナ
・ポルカノート株式会社
・株式会社ヴェルモンテ
・ハルネス株式会社
・株式会社ロザミオ
・株式会社エピフォルム
・華嶺泰股份有限公司(PELM ON RIVA CO.,LTD)
希望イメージ
シンプル 複雑
単色 カラフル
暗い 明るい
日常 高級
遊び心 厳粛
未来的 伝統的
女性的 男性的
希望する色
黒のテキストを希望します
納品ファイル
• 高解像度JPG (.jpg)
• イラストレーター形式 (.ai)
• フォトショップ形式 (.psd)
• PNG形式 (.png)
補足説明
添付にて参考までに名刺表面と既存の裏面データを送付します
当選者決定後のデータ入稿時ですが、以下の2点をお願いできますでしょうか。
------------------
①文字のアウトライン前のデータと、アウトライン済みのデータの2種類をお送
りください。
②jpg、pdfなどの見本データを一緒にお送りください。
------------------

またデザインにロゴ画像を使用していただいているご提案を当選とさせていただいた際には、
別途ロゴ画像データをお渡しいたしますので、入稿前に調整をお願いさせていただければと思います。
■ 選んだ理由

表面と並べた見たときのバランスの良さが一番のポイントとなりました。
また各コンテンツを読みやすく配置していただいており、営業の現場でもツールとして使いやすいのではないかと思ったことが選択の理由です。

■ 提案者全員のお礼・コメント

このたびは私どもの案件に多くのご提案をいただきありがとうございました。
素晴らしい提案が多く、選定に悩んでしまい、お時間をとってしまい申し訳ありませんでした。

今後もこのようなかたちでコンペを行うこともあるかと思いますが、また機会がありましたらぜひよろしくお願いいたします。

```html
<!DOCTYPE html>
<html lang="ja">
<head>
<meta charset="utf-8">
<title>名刺裏面 | 営業支援会社</title>
<link rel="stylesheet" href="https://fonts.googleapis.com/css2?family=Shippori+Mincho+B1:wght@700;800&family=Noto+Sans+JP:wght@400;700&display=swap">
<style>
  :root {
    --ink: #1a1a1a;
    --paper: #ffffff;
    --edge: #cfcfcf;
    --band-dark: #6b6b6b;
    --band-light: #d9d9d9;
    --band-text: #ffffff;
  }
  * { margin: 0; padding: 0; box-sizing: border-box; }
  html, body { width: 841px; height: 1200px; overflow: hidden; background: var(--paper); }
  .card {
    position: relative;
    width: 841px; height: 1200px;
    background: var(--paper);
    border: 2px solid var(--edge);
    color: var(--ink);
    font-family: "Noto Sans JP", sans-serif;
  }
  .catch {
    position: absolute; left: 60px; top: 58px;
    font-family: "Shippori Mincho B1", serif;
    font-weight: 800;
    line-height: 1;
    color: var(--ink);
  }
  .catch-line { display: block; white-space: nowrap; }
  .catch-line.lead { font-size: 74px; letter-spacing: 1px; }
  .catch-line.sub { font-size: 52px; margin-top: 48px; }
  .catch-line.sub.last { margin-top: 34px; }
  .catch .emph { font-size: 78px; }
  .band {
    position: absolute; left: 62px; width: 722px; height: 40px;
    background: linear-gradient(90deg, var(--band-dark) 0%, var(--band-dark) 50%, var(--band-light) 100%);
    color: var(--band-text);
    font-weight: 700; font-size: 23px; line-height: 40px;
    padding-left: 16px; letter-spacing: 1px;
  }
  .band.services { top: 424px; }
  .band.group { top: 846px; }
  .service-list {
    position: absolute; left: 70px; top: 478px; width: 700px;
    display: flex; flex-direction: column; gap: 6px;
  }
  .service-title {
    display: flex; align-items: center; gap: 8px;
    font-weight: 700; font-size: 27px; line-height: 1.25;
  }
  .service-title svg { width: 34px; height: 34px; flex: none; }
  .service-desc {
    margin-left: 42px; margin-top: 2px;
    font-size: 17.5px; line-height: 1.5;
  }
  .group-list {
    position: absolute; left: 80px; top: 904px;
    font-size: 19.5px; line-height: 1.62; list-style: none;
  }
</style>
</head>
<body>
<main class="card">
  <h1 class="catch">
    <span class="catch-line lead">日本で唯一</span>
    <span class="catch-line sub">新規営業に<span class="emph">特化</span>した</span>
    <span class="catch-line sub last"><span class="emph">営業支援</span>会社です。</span>
  </h1>

  <h2 class="band services">弊社サービス紹介</h2>

  <div class="service-list">
    <section class="service">
      <h3 class="service-title">
        <svg viewBox="0 0 40 40" aria-hidden="true"><rect x="3" y="9" width="27" height="27" fill="none" stroke="#1a1a1a" stroke-width="3"/><path d="M9 21 L16 29 L36 4" fill="none" stroke="#1a1a1a" stroke-width="5" stroke-linecap="square"/></svg>
        クヌーデル帳
      </h3>
      <p class="service-desc">日本で唯一、新規営業に特化した営業ツール。<br>営業会社自ら、現場の声と使いやすさをもとにシステム<br>を開発いたしました。</p>
    </section>

    <section class="service">
      <h3 class="service-title">
        <svg viewBox="0 0 40 40" aria-hidden="true"><rect x="3" y="9" width="27" height="27" fill="none" stroke="#1a1a1a" stroke-width="3"/><path d="M9 21 L16 29 L36 4" fill="none" stroke="#1a1a1a" stroke-width="5" stroke-linecap="square"/></svg>
        企業リスト作成
      </h3>
      <p class="service-desc">どんな営業活動も、まずはベストの営業先の見極めから。<br>社内、そしてWEBのデータを収集・分析を行ない、結果に<br>つながる、確度の高い企業リストを作成いたします。</p>
    </section>

    <section class="service">
      <h3 class="service-title">
        <svg viewBox="0 0 40 40" aria-hidden="true"><rect x="3" y="9" width="27" height="27" fill="none" stroke="#1a1a1a" stroke-width="3"/><path d="M9 21 L16 29 L36 4" fill="none" stroke="#1a1a1a" stroke-width="5" stroke-linecap="square"/></svg>
        FAX集客支援
      </h3>
      <p class="service-desc">中小企業、BtoBには非常に有効なFAXの原稿作成、また<br>FAX配信を代行いたします。</p>
    </section>
  </div>

  <h2 class="band group">グループ会社一覧</h2>

  <ul class="group-list">
    <li>株式会社クレモアリス・株式会社ミルベーナ</li>
    <li>ポルカノート株式会社・株式会社ヴェルモンテ</li>
    <li>ハルネス株式会社・株式会社ロザミオ</li>
    <li>株式会社エピフォルム</li>
    <li>華嶺泰股份有限公司（PELM ON RIVA CO.,LTD）</li>
  </ul>
</main>
</body>
</html>
```